Buch-/E-Book-Cover Autobiographische Kurzgeschichten
Zielgruppe
Ich vermarkte mein Buch selbst. Zielgruppe sind Frauen und Männer, die leichte Lektüre mit Humor und Lebenserfahrung lesen wollen.
Aufgabenstellung
Das Buch hat den Titel 'Sturmflut ohne Ende'.
Der Inhalt sind autobiographische Kurzgeschichten.
Erst verwitwet wagte ich einen Blick über den Zaun. Und tatsächlich war dort das Gras grüner, die Wiese enthielt lebenswichtige Kräuter und bunte Blumen. Da wollte ich hier, nur wie? Ich hatte „Zäune überwinden“ nicht gelernt. Versuch und Irrtum, Feldforschung, Kampf mit mir selbst, ein nie Aufgeben führten mich zum Erfolg, auf die andere Seite. Und die Wiese hält, was sie versprach. Da hatten sich doch der Witwentröster, das Datingportal, der Escort, den ich nicht mit aufs Zimmer nahm, die Aktfotos und und und gelohnt.
Meine autobiographischen Geschichten sind wie ein gutes Parfum mit Kopf-, Herz- und Basisnote. Riech doch einfach mal rein!
Mein Logo ist zu verwenden.
Einige Kurzgeschichten aus dem Buch stehen auf meiner Website, zum Reinlesen bei Bedarf.
Die Katastrophe, der Wendepunkt in meinem Leben, war der Tod meines Mannes.
Meine Website lautet : www.tann-wiese.de

```html
<!DOCTYPE html>
<html lang="de">
<head>
<meta charset="utf-8">
<title>Sturmflut ohne Ende – Buchcover</title>
<link rel="stylesheet" href="https://fonts.googleapis.com/css2?family=Oswald:wght@500&family=Great+Vibes&family=Montserrat:wght@500&display=swap">
<style>
  :root {
    --page-bg: #e9e7e4;
    --cover-white: #f7f7f6;
    --title-red: #b8323c;
    --title-gray: #8a8a8a;
    --ink: #1e1e1e;
    --sky: #f4f6f8;
    --facade-blue: #aebfd0;
    --facade-gray: #b9b9b9;
    --grass-green: #a9c85a;
    --grass-gray: #a3a3a3;
  }
  * { margin: 0; padding: 0; box-sizing: border-box; }
  html, body {
    width: 1200px; height: 1068px; overflow: hidden;
    background: var(--page-bg);
  }
  .book-cover {
    position: absolute; left: 256px; top: 34px;
    width: 688px; height: 1000px;
    background: linear-gradient(180deg, #ffffff 0%, var(--cover-white) 100%);
    overflow: hidden;
  }
  .cover-photo {
    position: absolute; left: 0; right: 0; top: 317px; bottom: 0;
    display: flex;
  }
  .cover-photo__colour {
    width: 359px;
    background: linear-gradient(180deg,
      var(--sky) 0%, var(--facade-blue) 30%, #c9d3dc 55%,
      #f3f6ea 70%, var(--grass-green) 82%, #cfe08c 100%);
  }
  .cover-photo__mono {
    flex: 1;
    background: linear-gradient(180deg,
      #f2f2f2 0%, var(--facade-gray) 30%, #cfcfcf 55%,
      #f4f4f4 70%, var(--grass-gray) 82%, #bdbdbd 100%);
  }
  .author-brand {
    position: absolute; left: 0; right: 0; top: 40px;
    display: flex; flex-direction: column; align-items: center; gap: 14px;
  }
  .author-brand__dot {
    width: 34px; height: 34px; border-radius: 50%;
    background: var(--title-red);
  }
  .author-brand__name {
    font-family: "Montserrat", sans-serif; font-weight: 500;
    font-size: 15px; letter-spacing: 1px;
    color: var(--title-red);
  }
  .cover-title {
    position: absolute; left: 0; top: 0; width: 688px; height: 560px;
  }
  .cover-title__word {
    font-family: "Oswald", sans-serif; font-weight: 500;
  }
  .cover-title__script {
    font-family: "Great Vibes", cursive;
  }
  .author-name {
    position: absolute; left: 0; right: 0; top: 946px;
    text-align: center;
    font-family: "Montserrat", sans-serif; font-weight: 500;
    font-size: 22px; letter-spacing: 3px;
    color: var(--ink);
  }
</style>
</head>
<body>
  <main class="book-cover">
    <div class="cover-photo" role="img" aria-label="Foto: Autorin im roten Kapuzenpullover lehnt links vor einem modernen Gebäude auf einer Wiese; linke Bildhälfte farbig, rechte schwarz-weiß">
      <div class="cover-photo__colour"></div>
      <div class="cover-photo__mono"></div>
    </div>

    <div class="author-brand">
      <span class="author-brand__dot"></span>
      <span class="author-brand__name">Elo Tann-Wiese</span>
    </div>

    <svg class="cover-title" viewBox="0 0 688 560" aria-label="Sturmflut ohne Ende">
      <defs>
        <clipPath id="left-half"><rect x="0" y="0" width="359" height="560"/></clipPath>
        <clipPath id="right-half"><rect x="359" y="0" width="329" height="560"/></clipPath>
      </defs>
      <g class="cover-title__words" stroke="#ffffff" stroke-width="2" paint-order="stroke">
        <g clip-path="url(#left-half)" fill="var(--title-red)">
          <text class="cover-title__word" x="91" y="330" font-size="196" textLength="502" lengthAdjust="spacingAndGlyphs">STURMFLUT</text>
          <text class="cover-title__word" x="200" y="515" font-size="196" textLength="330" lengthAdjust="spacingAndGlyphs">ENDE</text>
        </g>
        <g clip-path="url(#right-half)" fill="var(--title-gray)">
          <text class="cover-title__word" x="91" y="330" font-size="196" textLength="502" lengthAdjust="spacingAndGlyphs">STURMFLUT</text>
          <text class="cover-title__word" x="200" y="515" font-size="196" textLength="330" lengthAdjust="spacingAndGlyphs">ENDE</text>
        </g>
      </g>
      <text class="cover-title__script" x="330" y="378" font-size="104" text-anchor="middle"
            fill="var(--title-red)" stroke="#ffffff" stroke-width="5" paint-order="stroke"
            transform="rotate(-12 330 360)">ohne</text>
    </svg>

    <p class="author-name">AUTOR NAME</p>
  </main>
</body>
</html>
```